Brava-Lux.ch is looking for business card letterhead and envelope C5 with WOW effect

We need a strong business card for our company Brava-Lux.ch, logo is available. You want a black or dark background on which the logo Stark r% 26 # 252; appears. Letterhead and envelope in C5 format should be in a similar design, but does not have to be We need a strong business card for our company Brava-Lux.ch, logo is available. A black or dark background is desired, on which the logo Stark comes across. The letterhead and the envelope in C5 format should have a similar design.

Target Market(s)

Private customers as well as entrepreneurs

Contact Information for Business Card

E-mail: info@brava-lux.ch
Web.www.Brava-Lux.ch
Tel: +41 ( 0 ) 79 384 6027
Adresse:
Kellerweg 14
9405 Ostheim

Hier kann man Icons verwenden für Email,Tel und Adressse

Font styles to use
Other font styles liked:
• Dubai,bold

Colors

Designer to choose colors to be used in the design.

Requirements
Must have
• WOW effect
Nice to have
• R% 26 # 252; back business card with our service listings. - VEHICLE LABELING - SHOP WINDOW LABELING - STICKERS AND MUCH MORE ... in red color

```html
<!DOCTYPE html>
<html lang="en">
<head>
<meta charset="UTF-8">
<title>Brava-Lux.ch – Business Card</title>
<link rel="stylesheet" href="https://fonts.googleapis.com/css2?family=Poppins:wght@400;500;700&display=swap">
<style>
  :root {
    --bg: #161616;
    --card: #232323;
    --card-edge: #1c1c1c;
    --white: #ffffff;
    --yellow: #fdc718;
    --red: #ea2227;
    --faint: #2d2d2d;
    --rule: #8a8a8a;
  }
  * { box-sizing: border-box; margin: 0; padding: 0; }
  html, body { width: 1200px; height: 1200px; overflow: hidden; }
  body {
    background: radial-gradient(ellipse at 50% 35%, #262626 0%, var(--bg) 70%);
    font-family: "Poppins", sans-serif;
    color: var(--white);
    position: relative;
  }
  .card {
    position: absolute;
    left: 150px;
    width: 900px;
    height: 500px;
    background: linear-gradient(160deg, var(--card) 0%, var(--card-edge) 100%);
    box-shadow: 0 18px 40px rgba(0,0,0,.55);
    overflow: hidden;
  }
  .card--front { top: 70px; }
  .card--back { top: 630px; }

  .card__texture {
    position: absolute;
    right: 0;
    top: 0;
    width: 380px;
    height: 100%;
    background: radial-gradient(ellipse at 70% 50%, var(--faint) 0%, rgba(45,45,45,0) 70%);
  }

  .brand {
    font-weight: 700;
    color: var(--white);
    letter-spacing: 1px;
    text-transform: uppercase;
    display: flex;
    align-items: center;
    gap: 16px;
  }
  .brand__dot {
    width: 22px; height: 22px;
    background: var(--yellow);
    border-radius: 50%;
    flex: none;
  }

  .card--front .brand {
    position: absolute;
    left: 0; right: 0;
    top: 160px;
    justify-content: center;
    font-size: 56px;
  }
  .services {
    position: absolute;
    left: 0; right: 0;
    top: 300px;
    text-align: center;
    color: var(--red);
    font-weight: 700;
    font-size: 21px;
    letter-spacing: .5px;
    line-height: 1.6;
    text-transform: uppercase;
  }
  .services__item { display: inline-flex; align-items: center; gap: 10px; margin: 0 14px; }
  .services__item::before {
    content: "";
    width: 12px; height: 12px;
    background: var(--red);
    border-radius: 50%;
  }

  .card--back .brand {
    position: absolute;
    left: 70px;
    top: 170px;
    font-size: 36px;
  }
  .divider {
    position: absolute;
    left: 430px;
    top: 150px;
    width: 1px;
    height: 120px;
    background: var(--rule);
  }
  .contacts {
    position: absolute;
    left: 465px;
    top: 148px;
    list-style: none;
    font-size: 23px;
    font-weight: 500;
  }
  .contacts li { display: flex; align-items: center; gap: 16px; height: 42px; }
  .contacts svg { width: 30px; height: 30px; flex: none; }
  .address {
    position: absolute;
    left: 0; right: 0;
    bottom: 58px;
    text-align: center;
    font-size: 24px;
    font-weight: 500;
  }
  .card__band {
    position: absolute;
    left: 0; right: 0; bottom: 0;
    height: 20px;
    background: var(--red);
  }
</style>
</head>
<body>

<section class="card card--front">
  <div class="card__texture" role="img" aria-label="Faint dark decorative texture"></div>
  <div class="brand"><span class="brand__dot"></span>Brava-Lux.ch</div>
  <div class="services">
    <span class="services__item">Vehicle labeling</span>
    <span class="services__item">Shop window labeling</span><br>
    <span class="services__item">Stickers and much more</span>
  </div>
</section>

<section class="card card--back">
  <div class="card__texture" role="img" aria-label="Faint dark decorative texture"></div>
  <div class="brand"><span class="brand__dot"></span>Brava-Lux.ch</div>
  <div class="divider"></div>
  <ul class="contacts">
    <li>
      <svg viewBox="0 0 30 30" aria-hidden="true"><circle cx="15" cy="15" r="14" fill="#fdc718"/><path d="M10.5 8.5l3 .5 1 3.5-2 1.3a8 8 0 0 0 3.7 3.7l1.3-2 3.5 1 .5 3c-6 1.2-12.2-5-11-11z" fill="#232323"/></svg>
      +41 ( 0 ) 79 384 6027
    </li>
    <li>
      <svg viewBox="0 0 30 30" aria-hidden="true"><circle cx="15" cy="15" r="14" fill="#fdc718"/><rect x="8" y="10" width="14" height="10" fill="none" stroke="#232323" stroke-width="1.8"/><path d="M8 10l7 6 7-6" fill="none" stroke="#232323" stroke-width="1.8"/></svg>
      info@brava-lux.ch
    </li>
    <li>
      <svg viewBox="0 0 30 30" aria-hidden="true"><circle cx="15" cy="15" r="14" fill="#fdc718"/><g fill="none" stroke="#232323" stroke-width="1.6"><circle cx="15" cy="15" r="7"/><ellipse cx="15" cy="15" rx="3" ry="7"/><path d="M8 15h14"/></g></svg>
      www.Brava-Lux.ch
    </li>
  </ul>
  <p class="address">Kellerweg 14, 9405 Ostheim</p>
  <div class="card__band"></div>
</section>

</body>
</html>
```